Chicken Wing A0 and A4 Poster

Our restaurant name is Tovvra Grill

We have introduced chicken wings to our menu. They are deep fried and mixed with different sauce selections.

The sauce options are: Tovvra BBQ, Regular BBQ, Sweet Chili and Garlic, Hot Chili, Garlic

Available in a 6, 10 or 20 Pack.
Larger Catering Packs Available

We have uploaded some pictures from the internet with chicken wings.

We also have 4 other poster designs coming in the next 3 weeks.

Industry/Entity Type

Restaurant

```html
<!DOCTYPE html>
<html lang="en">
<head>
<meta charset="utf-8">
<title>Tovvra Grill – Chicken Wings Poster</title>
<link rel="stylesheet" href="https://fonts.googleapis.com/css2?family=PT+Sans:ital,wght@0,400;0,700;1,700&display=swap">
<style>
  :root {
    --wood-light: #c8925a;
    --wood-mid: #a8713f;
    --wood-dark: #7a4a24;
    --board: #b7773e;
    --board-edge: #8a5226;
    --paper: #efe2c8;
    --paper-shade: #d9c29a;
    --brand-red: #a3152b;
    --brand-faint: rgba(163,21,43,.22);
    --band-brown: #3e1a12;
    --band-red: #a3152b;
    --cream: #f6ecd6;
    --ink: #1c1410;
    --white: #ffffff;
  }
  * { margin: 0; padding: 0; box-sizing: border-box; }
  html, body {
    width: 1001px; height: 1200px; overflow: hidden;
    background: #2a2a2a;
    font-family: "PT Sans", Arial, sans-serif;
  }
  .poster { position: relative; width: 1001px; height: 1200px; overflow: hidden; }
  .wood-backdrop {
    position: absolute; inset: 0;
    background:
      radial-gradient(ellipse at 50% 30%, rgba(255,220,170,.35), transparent 60%),
      linear-gradient(180deg, var(--wood-light) 0%, var(--wood-mid) 55%, var(--wood-dark) 100%);
  }
  .brand-plaque {
    position: absolute; left: 199px; top: 57px; width: 564px; height: 240px;
    background: var(--paper);
    border: 6px solid var(--paper-shade);
    border-radius: 44px;
    box-shadow: 0 10px 24px rgba(60,30,10,.45);
    display: flex; flex-direction: column; align-items: center; justify-content: center;
  }
  .brand-name { font-weight: 700; font-size: 70px; color: var(--brand-red); line-height: 1; }
  .brand-tagline {
    margin-top: 10px; font-weight: 700; font-size: 18px; letter-spacing: 4px;
    color: var(--brand-red); text-transform: uppercase;
  }
  .headline-kicker, .headline-main {
    position: absolute; white-space: nowrap;
    transform: rotate(-12deg); transform-origin: left bottom;
    color: var(--brand-red); font-weight: 700; line-height: 1; text-transform: uppercase;
    text-shadow: 2px 2px 0 var(--cream), -2px -2px 0 var(--cream), 2px -2px 0 var(--cream), -2px 2px 0 var(--cream);
  }
  .headline-kicker { left: 32px; top: 388px; font-size: 40px; }
  .headline-main { left: 66px; top: 428px; font-size: 76px; }
  .headline-sub {
    position: absolute; left: 420px; top: 458px; white-space: nowrap;
    transform: rotate(-12deg); transform-origin: left top;
    color: var(--white); font-weight: 700; font-size: 27px; line-height: 1.25;
    text-transform: uppercase; text-shadow: 1px 1px 2px rgba(60,25,10,.6);
  }
  .info-band {
    position: absolute; left: 0; width: 510px;
    color: var(--white); font-weight: 700; font-style: italic;
    font-size: 37px; line-height: 1.27; padding-left: 40px;
    display: flex; flex-direction: column; justify-content: center;
    text-transform: uppercase;
  }
  .info-band--packs { top: 529px; height: 114px; background: var(--band-brown); }
  .info-band--catering { top: 661px; height: 130px; background: var(--band-red); }
  .wings-photo {
    position: absolute; left: 0; top: 820px; width: 640px; height: 380px;
    background: radial-gradient(ellipse at 40% 55%, #8a3416 0%, #6a2410 35%, #e9e5e0 62%, #c9b59a 100%);
  }
  .sauce-board { position: absolute; inset: 0; }
  .sauce-list {
    position: absolute; left: 560px; top: 540px; list-style: none;
    transform: rotate(-11deg); transform-origin: left top;
  }
  .sauce-list li {
    color: var(--brand-red); font-weight: 700; font-size: 60px; line-height: 82px;
    display: flex; align-items: center; gap: 16px; white-space: nowrap;
  }
  .sauce-list li::before {
    content: ""; width: 24px; height: 24px; border-radius: 50%; background: var(--brand-red); flex: none;
  }
  .contact {
    position: absolute; left: 690px; top: 990px;
    transform: rotate(-4deg); transform-origin: left top;
  }
  .contact-brand { font-weight: 700; font-size: 40px; color: var(--brand-faint); line-height: 1; }
  .contact-label { font-weight: 700; font-size: 27px; color: var(--ink); margin-top: 8px; }
  .contact-phone { font-weight: 700; font-size: 34px; color: var(--brand-red); }
</style>
</head>
<body>
<main class="poster">
  <div class="wood-backdrop" role="img" aria-label="Warm wooden plank texture background"></div>

  <header class="brand-plaque">
    <div class="brand-name">Tovvra Grill</div>
    <div class="brand-tagline">Authentic Lebanese Food</div>
  </header>

  <svg class="sauce-board" width="1001" height="1200" viewBox="0 0 1001 1200">
    <polygon role="img" aria-label="Wooden cutting board" points="470,420 1001,330 1001,1200 600,1200" fill="var(--board)" stroke="var(--board-edge)" stroke-width="6"/>
    <polygon role="img" aria-label="Torn parchment menu scroll" points="515,520 990,455 990,1150 600,1165" fill="var(--paper)"/>
  </svg>

  <h1>
    <span class="headline-kicker">Introduced</span>
    <span class="headline-main">Chicken Wings</span>
  </h1>

  <p class="headline-sub">Deep fried and mixed<br>with different sauce</p>

  <div class="info-band info-band--packs"><span>Available in</span><span>a 6, 10 or 20 pack.</span></div>
  <div class="info-band info-band--catering"><span>Larger catering</span><span>packs available</span></div>

  <div class="wings-photo" role="img" aria-label="Photo of glazed barbecue chicken wings on white plates"></div>

  <ul class="sauce-list">
    <li>Tovvra BBQ</li>
    <li>Regular BBQ</li>
    <li>Sweet Chili</li>
    <li>Hot Chili</li>
    <li>Garlic</li>
  </ul>

  <footer class="contact">
    <div class="contact-brand">Tovvra Grill</div>
    <div class="contact-label">CALL US NOW</div>
    <div class="contact-phone">000 0000 0000</div>
  </footer>
</main>
</body>
</html>
```